Website Design for a Graphic Design Studio in California

We are working with a graphic design company in California.
PLEASE NOTE: We report and ban any designer that reaches out directly to our customers.

Some sites to use for content/competitors and inspiration:

http://quelvint.co.uk
https://www.fendro.studio
https://www.zuplo.io (Client's Favorite)
https://www.merigoldcrafts.com
https://craftwimble.com
https://www.dravinsultonmask.com/us/home/

Thank you for taking the time to consider designing a website for us. We are web developers based in Stockton, CA, USA. Most of our projects go through the same process. Understanding this process may help you win a project with us. We custom-code all of our websites in-house. We don’t have any requirements as to what tools you use for your design, but we prefer Figma files. For any design that we label as four-stars, we send it to the client for review. The client picks the final design they want us to use. Once we complete this process, we will continue to show additional clients all the four-star sites and purchase them later. Your designs will have multiple chances to sell. For better chances of success, we ask that you follow these guidelines.

IMAGES:
If you use any images or icons in the design, we ask that you have a link to the asset so we can purchase the image/icon. Most of the designs we submit do not have the customer’s images on them unless they have some great images. Be creative; show us the feeling you are trying to portray with your image choices. Use any royalty-free site you choose. We subscribe to Tessaly and mainly use their images, but we can purchase images outside of Tessaly. PLEASE NOTE: we will not submit designs to clients with watermarks on the images.

FONTS:
We ask that you identify the fonts used in the design. This can be done in a message if you want. We typically use Brindle Fonts and Tessaly Fonts.

CONTENT:
We're always open to different content and ideas. We often submit designs with stock images so the client can see our vision. We typically take pictures after the website launch to use their images with our vision. Lorem Ipsum is fine for paragraphs, but we ask that you write the headers in correct English. We want to be able to show the vision and identify the sections of the website.

INSPIRATION:
We typically add a couple of links in the brief of websites we like to help you get started in your design.

REVISIONS:
We do not often ask for revisions of the designs unless we see something in the design that may not appeal to the client. If there are slight changes that we want to make, we do that in the development process.

FEEDBACK:
We rarely give feedback on designs during the design process. We are working on many website projects and do not have the time to provide feedback. We usually respond if your request is well thought out and asks specific questions, but a note asking “feedback, please” usually goes unanswered.

```html
<!DOCTYPE html>
<html lang="en">
<head>
<meta charset="utf-8">
<title>Vellorin Creative — Designing your tomorrow, today.</title>
<link href="https://fonts.googleapis.com/css2?family=Marcellus&family=Cormorant+Garamond:wght@400;500&display=swap" rel="stylesheet">
<style>
  :root {
    --paper: #eae8e3;
    --ink: #1f1d1b;
    --muted: #5b5853;
    --rule: #c9c6bf;
    --accent: #c98a3c;
    --accent-soft: #e7c9a0;
    --chip: #dcd9d3;
  }
  * { box-sizing: border-box; margin: 0; padding: 0; }
  html, body { width: 1200px; height: 2840px; overflow: hidden; background: var(--paper); }
  body { position: relative; font-family: "Cormorant Garamond", Georgia, serif; color: var(--ink); }
  .abs { position: absolute; }
  .display { font-family: "Marcellus", Georgia, serif; font-weight: 400; color: var(--ink); }

  /* header */
  .brand-name { font-family: "Cormorant Garamond", Georgia, serif; font-weight: 500; color: var(--ink); }
  .site-name { left: 165px; top: 22px; font-size: 20px; }
  .menu-button { left: 1002px; top: 20px; width: 28px; height: 28px; border-radius: 50%; background: var(--chip); }
  .menu-button::before, .menu-button::after { content: ""; position: absolute; left: 9px; width: 10px; height: 1.5px; background: var(--ink); }
  .menu-button::before { top: 11px; } .menu-button::after { top: 15px; }

  /* hero */
  .hero-art { left: 160px; top: 100px; width: 250px; height: 225px; border-radius: 8px; background: linear-gradient(135deg, #d8d5cf, #b9b6b0); }
  .hero-title { left: 420px; top: 220px; font-size: 49px; line-height: 1.15; }

  /* section labels */
  .section-rule { left: 165px; width: 870px; border-top: 1px solid var(--rule); padding-top: 12px; display: flex; justify-content: space-between; font-size: 17px; color: var(--muted); }

  .works-title { left: 165px; top: 632px; font-size: 50px; }
  .slider-arrow { top: 648px; width: 30px; height: 30px; border-radius: 50%; background: var(--chip); }
  .slider-arrow svg { display: block; margin: 9px; }
  .work-card { top: 712px; width: 432px; }
  .work-image { height: 246px; }
  .work-image.feather-gold { background: linear-gradient(120deg, #4a3526, #b08a5d 45%, #e4d7c4 60%, #6b4c33); }
  .work-image.feather-red { background: linear-gradient(135deg, #7c1f0f, #b4441e 50%, #e8a46b 80%, #f0b88a); }
  .work-caption { text-align: center; font-size: 22px; margin-top: 16px; }

  /* services */
  .services-title { left: 165px; top: 1198px; font-size: 50px; line-height: 1.2; }
  .services-art { left: 165px; top: 1395px; width: 310px; height: 165px; border-radius: 6px; background: linear-gradient(120deg, #e0ddd7, #b7b3ac); }
  .service-list { left: 630px; top: 1190px; width: 400px; list-style: none; }
  .service-list li { display: flex; justify-content: space-between; align-items: center; height: 67px; border-bottom: 1px solid var(--rule); font-size: 22px; }

  /* process */
  .process-title { left: 0; width: 1200px; top: 1778px; text-align: center; font-size: 56px; }
  .process-sub { left: 0; width: 1200px; top: 1852px; text-align: center; font-size: 15px; color: var(--muted); }
  .phase { top: 1922px; width: 290px; text-align: center; font-size: 18px; letter-spacing: 1px; text-transform: uppercase; }
  .phase.is-active { color: var(--accent); }
  .phase-rule { left: 165px; top: 1955px; width: 870px; height: 1px; background: var(--rule); }
  .phase-rule::before { content: ""; position: absolute; left: 0; top: -1px; width: 290px; height: 3px; background: var(--accent-soft); }
  .step { width: 290px; text-align: center; font-size: 17px; }
  .step-icon { width: 60px; height: 60px; margin: 0 auto 10px; border-radius: 50%; border: 1.5px solid var(--ink); display: flex; align-items: center; justify-content: center; }
  .step-icon::after { content: ""; width: 18px; height: 18px; border: 1.5px solid var(--ink); border-radius: 50%; }
  .step.is-active .step-icon, .step.is-active .step-icon::after { border-color: var(--accent); }
  .step-link { width: 1px; height: 30px; background: var(--ink); }
  .step-link.is-active { background: var(--accent); }

  /* footer */
  .footer-name { left: 0; width: 1200px; top: 2574px; text-align: center; font-size: 34px; }
  .footer-nav { left: 350px; top: 2650px; width: 500px; border-top: 1px solid var(--rule); border-bottom: 1px solid var(--rule); display: flex; }
  .footer-nav a { flex: 1; text-align: center; font-size: 16px; color: var(--ink); text-decoration: none; padding: 12px 0; border-right: 1px solid var(--rule); }
  .footer-nav a:last-child { border-right: none; }
  .social { top: 2718px; left: 0; width: 1200px; display: flex; justify-content: center; gap: 8px; }
  .social span { width: 26px; height: 26px; border-radius: 50%; background: var(--ink); }
  .copyright { left: 0; width: 1200px; top: 2790px; text-align: center; font-size: 13px; color: var(--muted); }
</style>
</head>
<body>

<header>
  <div class="abs brand-name site-name">Vellorin Creative</div>
  <div class="abs menu-button" aria-label="Menu"></div>
</header>

<section class="hero">
  <div class="abs hero-art" role="img" aria-label="Sketch illustration of a clipboard checklist with a pen"></div>
  <h1 class="abs display hero-title">Designing your tomorrow,<br>today.</h1>
</section>

<section class="works">
  <div class="abs section-rule" style="top:550px"><span>Works</span><span>01</span></div>
  <h2 class="abs display works-title">Featured work.</h2>
  <div class="abs slider-arrow" style="left:960px"><svg width="12" height="12" viewBox="0 0 12 12"><path d="M8 2 4 6l4 4" fill="none" stroke="#1f1d1b" stroke-width="1.5"/></svg></div>
  <div class="abs slider-arrow" style="left:996px"><svg width="12" height="12" viewBox="0 0 12 12"><path d="M4 2l4 4-4 4" fill="none" stroke="#1f1d1b" stroke-width="1.5"/></svg></div>
  <article class="abs work-card" style="left:167px">
    <div class="work-image feather-gold" role="img" aria-label="Close-up photo of a golden brown feather"></div>
    <p class="work-caption">Harbor ledger service</p>
  </article>
  <article class="abs work-card" style="left:603px">
    <div class="work-image feather-red" role="img" aria-label="Close-up photo of a red feather on a peach background"></div>
    <p class="work-caption">Featured work 02</p>
  </article>
</section>

<section class="services">
  <div class="abs section-rule" style="top:1122px"><span>Services</span><span>02</span></div>
  <h2 class="abs display services-title">If you can<br>imagine it, we<br>can design it.</h2>
  <div class="abs services-art" role="img" aria-label="Sketch illustration of a hand drawing with a pen"></div>
  <ul class="abs service-list">
    <li><span>01. Branding &amp; Strategy</span><span>+</span></li>
    <li><span>02. Logo design</span><span>+</span></li>
    <li><span>03. Packaging</span><span>+</span></li>
    <li><span>04. Style guides</span><span>+</span></li>
    <li><span>05. Illustration</span><span>+</span></li>
    <li><span>06. Marketing collateral</span><span>+</span></li>
  </ul>
</section>

<section class="process">
  <div class="abs section-rule" style="top:1705px"><span>Our process</span><span>03</span></div>
  <h2 class="abs display process-title">The Vellorin process.</h2>
  <p class="abs process-sub">9 steps to YOUR rebrand.</p>
  <div class="abs phase is-active" style="left:165px">Discover</div>
  <div class="abs phase" style="left:455px">Develop</div>
  <div class="abs phase" style="left:745px">Deliver</div>
  <div class="abs phase-rule"></div>

  <div class="abs step is-active" style="left:165px;top:1985px"><div class="step-icon"></div>1. Launch project</div>
  <div class="abs step-link is-active" style="left:310px;top:2100px"></div>
  <div class="abs step is-active" style="left:165px;top:2135px"><div class="step-icon"></div>2. Determine goals</div>
  <div class="abs step-link is-active" style="left:310px;top:2250px"></div>
  <div class="abs step is-active" style="left:165px;top:2285px"><div class="step-icon"></div>3. Formulate plan</div>

  <div class="abs step" style="left:455px;top:1985px"><div class="step-icon"></div>4. Analyzed brand</div>
  <div class="abs step-link" style="left:600px;top:2100px"></div>
  <div class="abs step" style="left:455px;top:2135px"><div class="step-icon"></div>5. Define identity</div>
  <div class="abs step-link" style="left:600px;top:2250px"></div>
  <div class="abs step" style="left:455px;top:2285px"><div class="step-icon"></div>6. Present creative</div>

  <div class="abs step" style="left:745px;top:1985px"><div class="step-icon"></div>7. Finalize creative</div>
  <div class="abs step-link" style="left:890px;top:2100px"></div>
  <div class="abs step" style="left:745px;top:2135px"><div class="step-icon"></div>8. Deliver toolkit</div>
  <div class="abs step-link" style="left:890px;top:2250px"></div>
  <div class="abs step" style="left:745px;top:2285px"><div class="step-icon"></div>9. Celebrate success</div>
</section>

<footer>
  <div class="abs section-rule" style="top:2490px"><span>Footer</span><span>04</span></div>
  <div class="abs brand-name footer-name">Vellorin Creative</div>
  <nav class="abs footer-nav">
    <a href="#">Home</a><a href="#">About us</a><a href="#">Portfolio</a><a href="#">Inspiration</a>
  </nav>
  <div class="abs social" aria-label="Social links"><span></span><span></span><span></span></div>
  <p class="abs copyright">Copyright 2024 Vellorin creative</p>
</footer>

</body>
</html>
```